Business Card Design

Contact Information for Business Card

A vertical business card request- a medium & light gray with silverpine tree logo (logo is attached)

Please use Trebuchet font -- if possible- can we use two different color gray? (See pictures attached below)
Info on the front should be the Silverpine tree logo - on the top of the card, followed by the info ...
Card to read: " " indicated what should be on the card --
Name: " Carla Merrow "
Title : "Partner "
" Office: 202.555.0147 "
" Mobile: 202.555.0183 "

Backside of the card - solid medium color gray color w/ address and small message centered in the card - Trebuchet font
to read:

" 718 B North Larkmoor Avenue, NE "
" Washington, DC 20019 "

Then below address to read:
" Fundraising | Event Planning | Political Consulting "

```html
<!DOCTYPE html>
<html lang="en">
<head>
<meta charset="utf-8">
<title>Silverpine Strategies – Business Card</title>
<link rel="stylesheet" href="https://fonts.googleapis.com/css2?family=Fira+Sans:wght@400;500;600&display=swap">
<style>
  :root {
    --gray-medium: #3e3e3e;
    --gray-light: #b1b1b1;
    --gray-mark: #5a5a5a;
    --gray-faint-start: rgba(90, 90, 90, 0);
    --gray-faint-end: rgba(90, 90, 90, 0.55);
    --ink-dark: #3a3a3a;
    --ink-light: #ffffff;
    --ink-soft: #c9c9c9;
    --page: #ffffff;
  }
  * { margin: 0; padding: 0; box-sizing: border-box; }
  html, body {
    width: 1200px;
    height: 1057px;
    overflow: hidden;
    background: var(--page);
    font-family: "Fira Sans", "Trebuchet MS", sans-serif;
  }
  .card {
    position: absolute;
    width: 411px;
    height: 718px;
    background: var(--gray-medium);
    overflow: hidden;
  }
  .card--front { left: 155px; top: 71px; }
  .card--back  { left: 637px; top: 221px; }

  .brand-mark {
    position: absolute;
    left: 165px;
    top: 90px;
    width: 190px;
    height: 190px;
    background: var(--gray-mark);
  }
  .brand {
    position: absolute;
    right: 18px;
    top: 296px;
    text-align: right;
    color: var(--ink-light);
    font-weight: 400;
  }
  .brand__name {
    display: block;
    font-size: 44px;
    line-height: 50px;
    letter-spacing: 6px;
    margin-right: -6px;
  }
  .brand__tagline {
    display: block;
    font-size: 24px;
    line-height: 28px;
    letter-spacing: 4px;
    margin-right: -4px;
  }

  .contact {
    position: absolute;
    left: 0;
    top: 414px;
    width: 100%;
    height: 304px;
    background: var(--gray-light);
    color: var(--ink-dark);
    padding: 44px 0 0 24px;
  }
  .contact__name {
    font-size: 26px;
    font-weight: 600;
    line-height: 32px;
    letter-spacing: 0.6px;
  }
  .contact__title {
    font-size: 23.5px;
    line-height: 40px;
    letter-spacing: 1px;
    margin-bottom: 38px;
  }
  .contact__line {
    font-size: 23.5px;
    line-height: 40px;
    letter-spacing: 1.5px;
  }

  .back-decoration {
    position: absolute;
    left: 137px;
    top: 300px;
    width: 274px;
    height: 418px;
    background: linear-gradient(to bottom, var(--gray-faint-start), var(--gray-faint-end));
  }
  .address {
    position: absolute;
    left: 0;
    width: 100%;
    top: 563px;
    text-align: center;
    color: var(--ink-soft);
    font-size: 21px;
    font-weight: 500;
    line-height: 29px;
    letter-spacing: 0.2px;
  }
  .services {
    position: absolute;
    left: 0;
    width: 100%;
    top: 641px;
    text-align: center;
    color: var(--ink-soft);
    font-size: 14.5px;
    font-weight: 500;
    letter-spacing: 0.8px;
  }
</style>
</head>
<body>
  <section class="card card--front" aria-label="Business card front">
    <div class="brand-mark" role="img" aria-label="Silverpine brand mark"></div>
    <div class="brand">
      <span class="brand__name">SILVERPINE</span>
      <span class="brand__tagline">STRATEGIES</span>
    </div>
    <div class="contact">
      <p class="contact__name">Carla Merrow</p>
      <p class="contact__title">Partner</p>
      <p class="contact__line">Office: 202.555.0147</p>
      <p class="contact__line">Mobile: 202.555.0183</p>
      <p class="contact__line">carla@silverpinellc.com</p>
    </div>
  </section>

  <section class="card card--back" aria-label="Business card back">
    <div class="back-decoration" role="img" aria-label="Faint brand decoration area"></div>
    <p class="address">718 B North Larkmoor Avenue, NE<br>Washington, DC 20019</p>
    <p class="services">Fundraising | Event Planning | Political Consulting</p>
  </section>
</body>
</html>
```